Brellow Business Card Re-design

Our current cards are outdated. This is our website www.brellowinsight.com. We would like something that is "on-brand" and consistent with our social media sites. We are strategic consultants with a core competency in Marketing Research. Although, please know we are considering a brand logo redesign and potentially a new look. If we like your work here we will invite you to participate when we get to that project. Thank you very much. Corabel
Here are our social sites: https://chirvalo.com/Brellow?lang=en
https://plus.quarnix.com/+Brellowinsight
https://www.workvelt.com/company/4958207/
https://www.friendlumo.com/BrellowInc/
Project Deadline Extended Reason: We appreciate the designs that have been submitted. We are extending the deadline because not everyone in our office has been available until now to view the designs. Thank you. Added Monday, September 25, 2017
Industry/Entity Type
Business
Look and feel

```html
<!DOCTYPE html>
<html lang="en">
<head>
<meta charset="utf-8">
<title>Brellow Business Card</title>
<link href="https://fonts.googleapis.com/css2?family=Lato:ital,wght@0,400;0,700;0,900;1,700&display=swap" rel="stylesheet">
<style>
  :root {
    --stage: #1b1b1b;
    --card-white: #ffffff;
    --card-brown: #4e3e2e;
    --card-brown-light: #5b4734;
    --brand-green: #5dbb46;
    --ink-brown: #3f3024;
    --text-light: #f4f1ec;
    --rule: #e9e4dc;
    --dot-blue: #1d8fd6;
    --dot-red: #dd4b39;
    --dot-navy: #1b6fa8;
    --dot-deep: #1d5b8f;
  }
  * { box-sizing: border-box; margin: 0; padding: 0; }
  html, body { width: 1200px; height: 1200px; overflow: hidden; }
  body {
    background: var(--stage);
    font-family: "Lato", Arial, sans-serif;
    position: relative;
  }
  .card {
    position: absolute;
    left: 180px;
    width: 840px;
    height: 480px;
  }
  .card--front { top: 90px; background: var(--card-white); }
  .card--back {
    top: 630px;
    background: linear-gradient(100deg, var(--card-brown) 0%, var(--card-brown-light) 100%);
    color: var(--text-light);
  }

  .brand {
    position: absolute;
    display: flex;
    align-items: center;
    gap: 18px;
  }
  .brand__name {
    font-weight: 900;
    color: var(--brand-green);
    letter-spacing: -2px;
    line-height: 1;
  }
  .brand__dot {
    border-radius: 50%;
    background: var(--brand-green);
  }
  .card--front .brand { left: 230px; top: 140px; }
  .card--front .brand__name { font-size: 120px; }
  .card--front .brand__dot { width: 34px; height: 34px; }

  .card--back .brand { left: 190px; top: 40px; }
  .card--back .brand__name { font-size: 140px; }
  .card--back .brand__dot { width: 40px; height: 40px; }

  .phone {
    position: absolute;
    display: flex;
    align-items: center;
    gap: 8px;
    color: var(--brand-green);
    font-weight: 700;
    font-style: italic;
  }
  .phone svg { fill: var(--brand-green); }
  .phone__bar { font-style: normal; font-weight: 400; }
  .card--front .phone { left: 234px; top: 280px; font-size: 34px; }
  .card--back .phone { left: 196px; top: 196px; font-size: 40px; }

  .contact {
    position: absolute;
    left: 0; right: 0;
    text-align: center;
    line-height: 1.2;
  }
  .contact__web { top: 262px; font-size: 36px; letter-spacing: 1px; }
  .contact__web .accent { color: var(--brand-green); }
  .contact__mail { top: 310px; font-size: 26px; letter-spacing: 0.5px; }

  .divider {
    position: absolute;
    left: 60px; right: 60px;
    top: 366px;
    height: 2px;
    background: var(--rule);
  }

  .social {
    position: absolute;
    left: 50px; right: 50px;
    top: 392px;
    display: flex;
    justify-content: space-between;
    align-items: center;
    list-style: none;
  }
  .social__item {
    display: flex;
    align-items: center;
    gap: 10px;
    font-size: 23px;
    letter-spacing: 0.5px;
  }
  .social__dot { width: 34px; height: 34px; border-radius: 50%; flex: none; }
  .social__dot--a { background: var(--dot-blue); }
  .social__dot--b { background: var(--dot-red); }
  .social__dot--c { background: var(--dot-navy); }
  .social__dot--d { background: var(--dot-deep); }
</style>
</head>
<body>

  <section class="card card--front" aria-label="Card front">
    <div class="brand">
      <span class="brand__name">Brellow</span>
      <span class="brand__dot"></span>
    </div>
    <div class="phone">
      <svg width="30" height="30" viewBox="0 0 24 24" aria-hidden="true"><path d="M6.6 10.8a15.1 15.1 0 0 0 6.6 6.6l2.2-2.2a1 1 0 0 1 1-.25 11.4 11.4 0 0 0 3.6.57 1 1 0 0 1 1 1V20a1 1 0 0 1-1 1A17 17 0 0 1 3 4a1 1 0 0 1 1-1h3.5a1 1 0 0 1 1 1c0 1.25.2 2.45.57 3.57a1 1 0 0 1-.25 1z"/></svg>
      <span class="phone__bar">|</span><span>407.555.0187</span>
    </div>
  </section>

  <section class="card card--back" aria-label="Card back">
    <div class="brand">
      <span class="brand__name">Brellow</span>
      <span class="brand__dot"></span>
    </div>
    <div class="phone">
      <svg width="34" height="34" viewBox="0 0 24 24" aria-hidden="true"><path d="M6.6 10.8a15.1 15.1 0 0 0 6.6 6.6l2.2-2.2a1 1 0 0 1 1-.25 11.4 11.4 0 0 0 3.6.57 1 1 0 0 1 1 1V20a1 1 0 0 1-1 1A17 17 0 0 1 3 4a1 1 0 0 1 1-1h3.5a1 1 0 0 1 1 1c0 1.25.2 2.45.57 3.57a1 1 0 0 1-.25 1z"/></svg>
      <span class="phone__bar">|</span><span>407.555.0187</span>
    </div>

    <p class="contact contact__web">www.<span class="accent">brellow</span>insight.com</p>
    <p class="contact contact__mail">brellowinsight@mailtrove.com</p>

    <div class="divider"></div>

    <ul class="social">
      <li class="social__item"><span class="social__dot social__dot--a"></span>Brellow</li>
      <li class="social__item"><span class="social__dot social__dot--b"></span>Brellowinsight</li>
      <li class="social__item"><span class="social__dot social__dot--c"></span>company/4958207/</li>
      <li class="social__item"><span class="social__dot social__dot--d"></span>BrellowInc</li>
    </ul>
  </section>

</body>
</html>
```